Web Design Project

Revamp current website adding newly designed logo and creating layout that is good on desktops, tablets, and cell phones.

Current website can be viewed at www.venkirainteriors.com

Will you see the website is small but graphics heavy in the gallery. The gallery needs to be setup so that it is easy to maintain the links and update the photos.

Needs to have high visual impact.

I need a new logo and website layout designed for my partner's business. This is a birthday present. His business is interior painting, wallpapering and design. He also has access to a wide variety of products including carpet, fabrics, furniture, wallpaper, tile, countertops, etc. I have attached some screen shots of his website for reference. He is a one man shop and has a stellar reputation with his customers. He is on-time, very tidy, excellent with animals, and always finishes on time and on budget. There are no restrictions on colors or fonts. The logo needs to work well with the website, business cards and printed materials. The website needs to flow content for device size so it looks just as good on a cell phone or tablet as it does on a desktop computer. Whatever the heck that's called! Thanks. I am looking forward to seeing everyone's ideas.

Target Market(s)

Consumers looking for interior design, painting, and wallpapering as well as interior products such as flooring, window treatments, reupholstering, counter tops, etc.

Industry/Entity Type

Cell Phone

Requirements
Must have
• Clean, sharp, visual impact (at least on the home page)
Should not have
• Clutter.

```html
<!DOCTYPE html>
<html lang="en">
<head>
<meta charset="utf-8">
<title>Venkira Interiors</title>
<link href="https://fonts.googleapis.com/css2?family=Marcellus&family=Kurale&family=Lato:wght@400;700&display=swap" rel="stylesheet">
<style>
:root{
  --stage:#3a2218;
  --paper:#efefef;
  --navy:#1f1a4d;
  --heading:#2b3575;
  --nav-red:#85131a;
  --accent-red:#b0322b;
  --bright-red:#e0453b;
  --footer-red:#b53a30;
  --ink:#3a3a3a;
  --rule:#dcdcdc;
  --fine-print:#f3c9a8;
  --black:#000;
  --white:#fff;
}
*{margin:0;padding:0;box-sizing:border-box}
html,body{width:1200px;height:1000px;overflow:hidden}
body{background:var(--stage);position:relative;font-family:"Kurale",serif}
.site{position:absolute;left:69px;top:46px;width:1052px;height:894px;background:var(--paper);box-shadow:0 6px 30px rgba(0,0,0,.6)}
.masthead{height:197px;background:linear-gradient(#f2f2f2 0%,#efefef 80%,#d8d6d3 100%);display:flex;align-items:center;justify-content:center;gap:18px}
.brand-mark{width:70px;height:70px;background:var(--navy)}
.brand-name{font-family:"Marcellus",serif;font-size:44px;color:var(--navy);letter-spacing:1px}
.main-nav{height:24px;background:var(--nav-red);display:flex;justify-content:center;gap:48px;padding-left:8px}
.main-nav a{font-family:"Lato",sans-serif;font-weight:700;font-size:8px;color:var(--white);text-decoration:none;line-height:23px}
.main-nav a.current{color:var(--black)}
.welcome{height:201px;text-align:center;padding-top:44px}
.welcome h1{font-family:"Marcellus",serif;font-weight:400;font-size:19px;color:var(--heading)}
.welcome p.intro{width:440px;margin:1px auto 0;font-size:8.6px;line-height:13px;color:var(--ink)}
.welcome p.tagline{margin-top:17px;font-size:12.5px;color:var(--ink);letter-spacing:.3px}
.showcase{position:relative;height:242px}
.showcase svg{position:absolute;left:0;top:0}
.features{position:absolute;left:600px;top:32px;width:150px}
.feature{font-size:13px;font-weight:700;color:var(--accent-red);line-height:17px;position:absolute;white-space:nowrap}
.rule{position:absolute;width:52px;height:3px;background:var(--rule)}
.estimate{position:absolute;top:724px;left:0;width:1052px;height:94px;background:var(--black);text-align:center;font-family:"Kurale",serif;font-weight:700;font-size:11px;line-height:14px;padding-top:16px}
.estimate .lead{color:var(--white)}
.estimate .area{color:var(--bright-red)}
.estimate .call{margin-top:3px;color:var(--bright-red);display:flex;justify-content:center;align-items:center;gap:14px}
.estimate .call .line{width:62px;height:2px;background:#d9d9d9}
.estimate .call b{color:var(--white)}
.site-footer{position:absolute;top:818px;left:0;width:1052px;height:76px;background:var(--footer-red);text-align:center;padding-top:22px}
.social{display:flex;justify-content:center;gap:8px;padding-left:12px}
.social span{width:6px;height:6px;border-radius:50%;background:var(--white)}
.copyright{margin-top:9px;font-family:"Lato",sans-serif;font-size:6.5px;color:var(--fine-print);letter-spacing:.7px}
</style>
</head>
<body>
<div class="site">
  <header class="masthead">
    <div class="brand-mark"></div>
    <div class="brand-name">Venkira Interiors</div>
  </header>
  <nav class="main-nav">
    <a class="current" href="#">Home</a>
    <a href="#">About</a>
    <a href="#">Services</a>
    <a href="#">Contact</a>
  </nav>
  <section class="welcome">
    <h1>Welcome to Venkira Interiors</h1>
    <p class="intro">With over 20 years of experience in the carpentry trade, we provide workmanship for the domestic and commercial markets. Whether you are starting with a small project or a large project, I am ready to bring your ideas to life. It doesn't take a big budget to achieve dramatic effects.</p>
    <p class="tagline">A wonderful new look is within anyone's reach.</p>
  </section>
  <section class="showcase">
    <svg width="1052" height="242" viewBox="0 0 1052 242">
      <defs>
        <linearGradient id="roomA-wall" x1="0" y1="0" x2="1" y2="0">
          <stop offset="0" stop-color="#d6d2d0"/><stop offset=".12" stop-color="#e9e8e6"/>
          <stop offset=".7" stop-color="#e4e3e2"/><stop offset=".95" stop-color="#f7f7f5"/><stop offset="1" stop-color="#ececea"/>
        </linearGradient>
        <linearGradient id="roomA-floor" x1="0" y1="0" x2="0" y2="1">
          <stop offset="0" stop-color="#dcdcdf" stop-opacity="0"/><stop offset="1" stop-color="#cfcfd4"/>
        </linearGradient>
        <linearGradient id="roomB-base" x1="0" y1="0" x2="1" y2="0">
          <stop offset="0" stop-color="#4a2414"/><stop offset=".12" stop-color="#6b3620"/>
          <stop offset=".2" stop-color="#c9c4b4"/><stop offset=".75" stop-color="#d9d5c6"/><stop offset="1" stop-color="#e2ded0"/>
        </linearGradient>
        <linearGradient id="roomB-shade" x1="0" y1="0" x2="0" y2="1">
          <stop offset="0" stop-color="#5c3220" stop-opacity=".75"/><stop offset=".35" stop-color="#8a6a52" stop-opacity=".25"/>
          <stop offset=".65" stop-color="#ffffff" stop-opacity="0"/><stop offset="1" stop-color="#efe9d6" stop-opacity=".6"/>
        </linearGradient>
        <linearGradient id="roomC-base" x1="0" y1="0" x2="1" y2="0">
          <stop offset="0" stop-color="#ede3cf"/><stop offset=".45" stop-color="#f1e8d6"/>
          <stop offset=".72" stop-color="#e4cfb4"/><stop offset=".85" stop-color="#b98261"/><stop offset="1" stop-color="#d8c7b0"/>
        </linearGradient>
        <linearGradient id="roomC-floor" x1="0" y1="0" x2="0" y2="1">
          <stop offset="0" stop-color="#ffffff" stop-opacity="0"/><stop offset=".7" stop-color="#ffffff" stop-opacity=".1"/><stop offset="1" stop-color="#f2ece2" stop-opacity=".7"/>
        </linearGradient>
        <linearGradient id="roomD" x1="0" y1="0" x2="0" y2="1">
          <stop offset="0" stop-color="#e6e1d6"/><stop offset=".6" stop-color="#d8cfbf"/><stop offset="1" stop-color="#c9bba6"/>
        </linearGradient>
      </defs>
      <rect width="1052" height="242" fill="#efefef"/>
      <g role="img" aria-label="Photo of an empty freshly painted bedroom with ceiling fan">
        <rect x="0" y="0" width="362" height="242" fill="url(#roomA-wall)"/>
        <rect x="0" y="0" width="362" height="242" fill="url(#roomA-floor)"/>
      </g>
      <g role="img" aria-label="Photo of a bedroom with a wooden four-poster bed">
        <polygon points="362,0 629,0 567,242 362,242" fill="url(#roomB-base)"/>
        <polygon points="362,0 629,0 567,242 362,242" fill="url(#roomB-shade)"/>
      </g>
      <g role="img" aria-label="Photo of a wall-mounted desk with a chair and wooden hutch">
        <polygon points="761,0 1009,0 1009,242 701,242" fill="url(#roomC-base)"/>
        <polygon points="761,0 1009,0 1009,242 701,242" fill="url(#roomC-floor)"/>
      </g>
      <rect x="1009" y="0" width="43" height="242" fill="url(#roomD)" role="img" aria-label="Photo of a room interior detail"/>
    </svg>
    <div class="features">
      <div class="feature" style="left:42px;top:2px">High Quality<br>Materials</div>
      <div class="rule" style="left:32px;top:50px"></div>
      <div class="feature" style="left:24px;top:71px">Satisfaction<br>Guaranteed</div>
      <div class="rule" style="left:14px;top:119px"></div>
      <div class="feature" style="left:5px;top:140px">Affordable<br>Prices</div>
    </div>
  </section>
  <section class="estimate">
    <div class="lead">Get a free estimate!</div>
    <div class="area">Servicing portions of Jackson, Johnson,<br>and Wyandotte counties</div>
    <div class="call"><span class="line"></span><span>Call Now: <b>(913) 555-0148</b></span><span class="line"></span></div>
  </section>
  <footer class="site-footer">
    <div class="social"><span></span><span></span><span></span></div>
    <p class="copyright">© 2014 Venkira Interiors. All rights reserved.</p>
  </footer>
</div>
</body>
</html>
```